Für das neue Tantra-Bildungszetrum: 8-oder 10-Seiten-Faltblatt und ein Plakat DIN A3
Zielgruppe
Es geht darum, über das Angebot des neuen Bildungszentrums Haus der Lichtung zu informieren.
Das Zentrum organisiert und führt regelmäßige Veranstaltungen wie Info-Vorträge, Schnuppertage, Seminare, Kurse und Intensivtrainings durch, ist in allem spezialisiert auf Tantra. Das Zentrum ist vertreten an mehreren Standorten Deutschlands durch das jeweils ein Team an Lehrern und Dozenten. Für die Veranstaltungen werden externe Räume angemietet. Das Angebot soll in jeder Stadt, wo die Broschüren oder Faltblätter verteilt werden. Die Anmeldung und Registrierung erfolgt über die neue Homepage, die bald freigegeben wird und noch nicht zur Verfügung steht.
Das Besondere am Zentrum ist die Möglichkeit, eigene tantrische Selbsterfahrungen zu machen und entweder später oder als Option sich gleich für einen der sechs neuen Tantra- Ausbildungsberufe zu entscheiden.
Darüber hinaus, soll die Broschüre oder die Faltblätter zur Mitarbeit und Kooperation mit selbständigen Yoga- und Tantra-Lehrern, sowie Ärzten, Therapeuten und Heilpraktiken einladen.
Das Bildungszentrum ist ein Netzwerk der Honorar-Dozenten, die entweder Lehrer und Experte auf dem tantrischen Bereich oder Vertreter der klassischen und alternativen Heilkunde oder beides zusammen sind.
Wer ist die Zielgruppe? Männer und Frauen, vom 18 - 60 Jahre. Menschen, die sich für Tantra und Selbsterfahrung interessieren, und Menschen, die nach einer neuen beruflichen Perspektive suchen.
Aufgabenstellung
1). 10-Seiten- Faltblatt designen
2). Plakat DIN A3 gestalten

```html
<!DOCTYPE html>
<html lang="de">
<head>
<meta charset="utf-8">
<title>Haus der Lichtung – Faltblatt</title>
<link href="https://fonts.googleapis.com/css2?family=Rokkitt:wght@400;600;700&display=swap" rel="stylesheet">
<style>
:root{
  --teal:#0f5f5b;
  --teal-soft:#6f9f9c;
  --orange:#ef7d22;
  --orange-soft:#e9a56c;
  --paper:#f6f6f5;
  --paper-shade:#e9e9e8;
  --ink:#3a3a3a;
  --bg:#e8e8e8;
  --photo-a:#c8742e;
  --photo-b:#7a2c1c;
}
*{box-sizing:border-box}
html,body{margin:0;width:702px;height:1200px;overflow:hidden;background:var(--bg);font-family:"Rokkitt",serif;color:var(--ink)}
.canvas{position:relative;width:702px;height:1200px}
.panel{position:absolute;background:linear-gradient(90deg,#fdfdfc,var(--paper-shade));overflow:hidden}
.abs{position:absolute}
.photo{position:absolute;background:radial-gradient(circle at 40% 40%,#f2a24a,var(--photo-a) 45%,var(--photo-b))}
.portrait{position:absolute;border-radius:50%;background:radial-gradient(circle,#b98a6c,#5b3b2c);border:1.5px solid var(--orange)}
.icon{display:block;border-radius:50%;margin:0 auto}
.icon-orange{width:15px;height:15px;border:1px solid var(--orange);background:rgba(239,125,34,.12)}
.icon-light{width:13px;height:13px;border:1px solid rgba(255,255,255,.6);background:rgba(255,255,255,.12)}
.brand{position:absolute;display:flex;align-items:center;gap:3px}
.brand-dot{width:9px;height:9px;border-radius:50%;background:var(--orange)}
.brand-text{font-weight:700;color:var(--teal);line-height:1}
.brand-text small{display:block;font-weight:700;color:var(--teal)}
.slogan{color:#fff;font-weight:700;font-size:4.6px;line-height:1.25;text-align:center}
.tab{position:absolute;writing-mode:vertical-rl;color:#fff;font-weight:600;font-size:9px;display:flex;align-items:center;padding-top:8px;white-space:nowrap}
.tab-teal{background:var(--teal)}
.tab-orange{background:var(--orange)}
.card{position:absolute;text-align:center}
.card h3{margin:2px 0 0;font-size:5px;font-weight:700;color:var(--teal);line-height:1.15}
.card h4{margin:0;font-size:4.8px;font-weight:400;color:var(--orange);line-height:1.15}
.body{margin:3px 0 0;font-size:3.9px;line-height:1.3;text-align:justify}
.rowhead{position:absolute;display:flex;align-items:center;gap:3px;font-size:4.6px;font-weight:700;white-space:nowrap}
.rowhead i{display:block;height:4px}
.footline{position:absolute;display:flex;align-items:center;gap:5px;font-size:4.2px;color:var(--teal);white-space:nowrap}
.footline span{color:var(--orange)}
.contact{position:absolute;font-size:5px;font-weight:700;color:var(--teal);line-height:1}
.contact h5{margin:0 0 3px;font-size:5.6px}
.contact div{display:flex;align-items:center;gap:4px;margin-bottom:3px}
.contact i{display:block;width:5px;height:5px;border-radius:50%;background:var(--teal)}
.network{position:absolute;font-size:4.3px;font-weight:700;color:var(--orange)}
.intro{position:absolute;font-size:4.2px;line-height:1.3;color:#666;text-align:justify}
.wave{position:absolute;left:0;display:block}
</style>
</head>
<body>
<div class="canvas">

<!-- ===== Folded front: cover panel ===== -->
<section class="panel cover" style="left:122px;top:88px;width:118px;height:314px">
  <div class="brand" style="left:22px;top:30px">
    <span class="brand-dot"></span>
    <span class="brand-text" style="font-size:7px"><small style="font-size:5px;font-weight:400;color:var(--orange)">Bildungszentrum</small>Haus der Lichtung</span>
  </div>
  <div class="photo" role="img" aria-label="Rundes Foto eines Paares in warmem Licht, umgeben von orangefarbenem Mandala" style="left:25px;top:80px;width:64px;height:64px;border-radius:50%;border:2px solid var(--orange)"></div>
  <svg class="wave" style="top:150px" width="118" height="16" viewBox="0 0 118 16"><path d="M0 8 Q30 16 60 9 T118 2 V16 H0Z" fill="var(--teal)"/><path d="M0 7 Q30 15 60 8 T118 1" fill="none" stroke="var(--orange)" stroke-width="1.5"/></svg>
  <div class="abs" style="left:0;top:165px;width:118px;height:149px;background:var(--teal);display:flex;flex-direction:column;align-items:center;gap:5px;padding-top:4px">
    <span class="icon icon-light" role="img" aria-label="Mandala-Symbol"></span>
    <div class="slogan">Tantra als Weg der<br>Transformation</div>
    <span class="icon icon-light" role="img" aria-label="Mandala-Symbol"></span>
    <div class="slogan">Verändere durch Tantra<br>dein Leben, deine Beziehungen,<br>dein Job!</div>
    <span class="icon icon-light" role="img" aria-label="Mandala-Symbol"></span>
    <div class="slogan">Nutze Tantra für mehr Erfolg,<br>Kraft, Energie und Lust am Leben!</div>
  </div>
</section>
<div class="tab tab-teal" style="left:239px;top:88px;width:14px;height:152px;font-size:8px">Info - Vorträge</div>
<div class="tab tab-orange" style="left:239px;top:240px;width:14px;height:162px;font-size:8px">In Tantra schnuppern</div>
<div class="tab tab-teal" style="left:253px;top:88px;width:13px;height:152px;font-size:8px">12 - Wochen Kurse</div>
<div class="tab tab-orange" style="left:253px;top:240px;width:13px;height:162px;font-size:8px">Jahrestraining</div>

<!-- ===== Back panel ===== -->
<section class="panel back" style="left:432px;top:88px;width:147px;height:314px">
  <div class="abs" style="left:0;top:0;width:147px;height:81px;background:var(--teal);padding-top:25px">
    <span class="icon icon-light" style="width:20px;height:20px" role="img" aria-label="Mandala-Symbol"></span>
    <div class="slogan" style="margin-top:5px">Erlebe und erfahre, wie Tantra dein Weg der<br>Trantsformation zu mehr Freude, Lebendig-<br>keit, Erfolg, Kraft, Liebe und Lust werden kann.</div>
  </div>
  <div class="photo" role="img" aria-label="Foto: Hände bei einer Massage auf rotem Tuch" style="left:0;top:81px;width:147px;height:92px"></div>
  <svg class="wave" style="top:162px" width="147" height="14" viewBox="0 0 147 14"><path d="M0 10 Q40 2 80 7 T147 4 V0 H0Z" fill="var(--photo-b)" opacity="0"/><path d="M0 8 Q40 0 80 6 T147 3 V14 H0Z" fill="#fbfbfb"/><path d="M0 8 Q40 0 80 6 T147 3" fill="none" stroke="var(--teal)" stroke-width="2"/></svg>
  <div class="portrait" role="img" aria-label="Porträtfoto einer Lehrerin" style="left:8px;top:187px;width:38px;height:38px"></div>
  <div class="intro" style="left:53px;top:188px;width:86px">Du findest uns an unterschiedlichen Standorten Deutschlands und in deiner Stadt, wenn du dieses Faltblatt gefunden hast.<br><br>Für unsere Angebote mieten wir geeignete Räume in Berlin, Leipzig, Hamburg, Dresden und bald in deiner Stadt.</div>
  <div class="contact" style="left:12px;top:238px">
    <h5>Kontakt:</h5>
    <div><i></i>www.lichtung-tantra.de</div>
    <div><i></i>0151 23 45 67 80</div>
    <div><i></i>Tantrisches.Bildungszentrum.HausDerLichtung</div>
    <div><i></i>HausDerLichtung</div>
  </div>
  <div class="network" style="left:10px;top:292px">Wir sind ein wachsendes Netzwerk aus mehreren Lehrern.</div>
</section>

<!-- ===== Inner spread 1 ===== -->
<section class="panel spread" style="left:72px;top:450px;width:263px;height:314px">
  <div class="abs" style="left:116px;top:0;width:1px;height:314px;background:#ddd"></div>
  <div class="rowhead" style="left:0;top:15px;color:var(--teal)"><i style="width:74px;background:var(--teal)"></i>1 x im Monat finden unsere Vorträge in deiner Stadt statt.</div>
  <div class="card" style="left:14px;top:28px;width:94px">
    <span class="icon icon-orange" role="img" aria-label="Mandala-Symbol"></span>
    <h3>Info-Vortrag</h3><h4>„Was ist Tantra?"</h4>
    <p class="body">Tantra? Was bedeutet es? Wo kommt es her? Wie kann Tantra dein Leben bereichern? Während unseres Infovortrages zum Thema Tantra erhältst du theoretisches Wissen über die Philosophie und geschichtliche Entwicklung des Tantra sowie seinen Strömungen und Techniken. Ohne an einem unserer Seminare oder Kurse teilnehmen zu müssen, kannst du dich hier in angenehm entspannter Atmosphäre darüber informieren, was sich hinter dem Begriff Tantra verbirgt, eventuelle Vorurteile über den Begriff korrigieren und dein Allgemeinwissen erweitern.</p>
  </div>
  <div class="card" style="left:124px;top:22px;width:96px">
    <span class="icon icon-orange" role="img" aria-label="Mandala-Symbol"></span>
    <h3>Vortrag über</h3><h4>berufliche Perspektiven</h4>
    <p class="body">Mach Tantra zu deinem Beruf! Informiere dich über unsere Ausbildungsangebote und über die beruflichen Perspektiven, die sich dir nach Abschluss einer unserer Ausbildungen eröffnen. Aus sechs unterschiedlichen Berufen kannst du die Ausbildung wählen, die dich am meisten anspricht. Während des Vortrages erhältst du Einblick über den Inhalt und die Möglichkeiten, die aus den jeweiligen Ausbildungen entstehen. Bitte melde dich zu einem der nächsten Vorträge an. Die Vorträge bieten wir an unterschiedlichen Standorten an. Suche dir aus dem Angebot den für dich passenden Ort und Termin heraus.</p>
  </div>
  <div class="rowhead" style="left:0;top:138px;color:var(--orange)"><i style="width:135px;background:var(--orange)"></i>Mehrmals im Monat finden statt:</div>
  <div class="card" style="left:14px;top:150px;width:94px">
    <span class="icon icon-orange" role="img" aria-label="Mandala-Symbol"></span>
    <h3>Tantra-Schnuppertag</h3><h4>„Der Geschmack von Tantra"</h4>
    <p class="body">Erhalte Einblick in Philosophie und Geschichte von Tantra und bekomme einen lebendigen Vorgeschmack auf tantrisches Erleben. Wenn du an unserem Tantraschnuppertag teilnimmst, erhältst du einen Überblick zur Philosophie und geschichtlichen Entwicklung des Tantra sowie seinen Strömungen. Ausserdem bekommst du einen ersten Einblick in dessen Techniken. Die Durchführung verschiedener Übungen während des Tages zielt darauf ab, dir einen körperlich erlebten Vorgeschmack auf die Inhalte der angebotenen Tantrakurse oder des Tantrajahrestrainings zu geben.</p>
  </div>
  <div class="card" style="left:124px;top:150px;width:96px">
    <span class="icon icon-orange" role="img" aria-label="Mandala-Symbol"></span>
    <h3>Einsteiger-Wochenende</h3><h4>„Die Farbe, der Klang und Geruch von Tantra"</h4>
    <p class="body">In unserem zweitägigen Einsteigerseminar wird dir unter fürsorglicher Anleitung viel Raum für das eigene Erleben tantrischer Realitätsbetrachtung gegeben. Du lernst, deine Wahrnehmung von dir selbst und anderen zu verändern, zu schärfen und zu fokussieren. Es bietet mehr praktisches Erleben als der Schnuppertag und ermöglicht mehr tantrische Wahrnehmung mit allen Sinnen.</p>
  </div>
  <div class="footline" style="left:16px;top:293px"><span class="brand-dot" style="width:6px;height:6px"></span><b style="font-size:4.6px">Haus der Lichtung</b> Alle Termine und Angebote findest du auch hier: <span>www.lichtung-tantra.de</span></div>
</section>
<div class="tab tab-teal" style="left:299px;top:450px;width:22px;height:140px">Info - Vorträge</div>
<div class="tab tab-orange" style="left:299px;top:590px;width:22px;height:174px">In Tantra schnuppern</div>
<div class="tab tab-teal" style="left:321px;top:450px;width:14px;height:140px;font-size:8px">12 - Wochen Kurse</div>
<div class="tab tab-orange" style="left:321px;top:590px;width:14px;height:174px;font-size:8px">Jahrestraining</div>

<!-- ===== Inner spread 2 ===== -->
<section class="panel spread" style="left:373px;top:450px;width:278px;height:314px">
  <div class="abs" style="left:132px;top:0;width:1px;height:314px;background:#ddd"></div>
  <div class="card" style="left:8px;top:14px;width:118px">
    <span class="icon icon-orange" role="img" aria-label="Mandala-Symbol"></span>
    <h3>Anfängerkurs</h3>
    <p class="body">Gönne dir zwölf Abende für den Beginn deiner tantrischen Selbstentwicklung. Tauche ein in Theorie und tantrische Praxis. Über zwölf Wochen hinweg wird dir an jeweils einem Wochentag während drei Stunden ermöglicht, einen Einblick in die Welt des Tantra zu bekommen sowie praktische Erfahrung zu machen.</p>
    <span class="icon icon-orange" style="margin-top:6px" role="img" aria-label="Mandala-Symbol"></span>
    <h3>Mittelstufe</h3>
    <p class="body">Schreite weiter auf dem tantrischen Pfad. Überwinde deine Scham und erlebe bewusste Nacktheit im geschützten Raum. Nimm dich lebendiger wahr und spüre den Kontakt mit anderen auf eine neue bereichernde Weise. Genau wie der Anfängerkurs findet das Mittelstufekurs über zwölf Wochen hinweg während drei Stunden eines Wochentages statt.</p>
  </div>
  <div class="card" style="left:140px;top:14px;width:116px">
    <span class="icon icon-orange" role="img" aria-label="Mandala-Symbol"></span>
    <h3>Fortgeschrittene</h3>
    <p class="body">Erlerne sexuelle Praktiken und die tantrische Nutzung deiner sexuellen Energie. Auch das Seminar für Fortgeschrittene findet über zwölf Wochen hinweg während drei Stunden eines Wochentages statt. Das Hauptthema dieses Kurses sind sexuelle Praktiken. Du erhältst eine Einführung in tantrische sexuelle Praktiken und in die tantrische Nutzung der sexuellen Energie. Im Kurs finden keine sexuelle Interaktionen statt. Du bekommst Anleitungen und Anregungen zu tantrischen Praktiken; üben dieser Praktiken findet nicht im Rahmen des Kurses statt.</p>
  </div>
  <div class="footline" style="left:140px;top:131px;font-size:4px"><span class="brand-dot" style="width:6px;height:6px"></span><b style="font-size:4.4px">Haus der Lichtung</b><span style="color:var(--teal);white-space:normal;width:70px;display:block">Alle Termine und Angebote findest du auch hier: <span>www.lichtung-tantra.de</span></span></div>
  <div class="rowhead" style="left:0;top:138px;color:var(--orange)"><i style="width:111px;background:var(--orange)"></i>Zwei Mal im Jahr beginnt ein neues Tantra-Jahrestraining</div>
  <div class="card" style="left:8px;top:153px;width:118px">
    <span class="icon icon-orange" role="img" aria-label="Mandala-Symbol"></span>
    <h3>Tantra-Jahrestraining</h3>
    <p class="body">Im Jahrestraining gehst du mit zehn intensiven verlängerten Wochenenden in die Erfahrung ausgedehnter tantrischer sexueller Praxis. Die Gruppe derer, die unser Jahrestraining absolvieren, trifft sich zu zehn Terminen für jeweils ein verlängertes Wochenende von Freitag bis Sonntag. Während unseres Jahrestrainings erlebst du die intensive Beschäftigung mit tantrischen Techniken, die verstärkt ihren Fokus auf tantrischer sexueller Praxis hat. Die zehn Treffen stellen eine intensive Selbsterfahrung mit transformierendem Charakter dar.</p>
  </div>
  <div class="card" style="left:140px;top:153px;width:116px">
    <span class="icon icon-orange" role="img" aria-label="Mandala-Symbol"></span>
    <h3>Tantra - Retreats</h3>
    <p class="body">Tantra Retreats – intensive Erfahrungen der Innenwelt. Möchtest du dich innerhalb von kurzer Zeit sehr intensiv erkennen und erfahren? Wenn ja, dann ist ein Tantra Retreat genau das Richtige für dich. Über mehrere Tage hinweg wirst du in die Welt der Gefühle, des Bewusstseins und der Liebe eintauchen. Du legst für die Zeit des Retreats alle deine Verpflichtungen ab und widmest dich deinem Inneren. Diese Tage des Rückzugs ermöglichen einen weitgreifenden inneren Wandel bei jedem Einzelnen der Gruppe.</p>
  </div>
  <div class="footline" style="left:10px;top:293px"><span class="brand-dot" style="width:6px;height:6px"></span><b style="font-size:4.6px">Haus der Lichtung</b> Erfahre auf <span>www.lichtung-tantra.de</span>, wann die nächste Jahresgruppe in deiner Stadt beginnt</div>
</section>
<div class="tab tab-teal" style="left:629px;top:450px;width:22px;height:140px">12 - Wochen Kurse</div>
<div class="tab tab-orange" style="left:629px;top:590px;width:22px;height:174px">Jahrestraining</div>

<!-- ===== Outer spread ===== -->
<section class="panel outer" style="left:85px;top:813px;width:525px;height:331px">
  <!-- panel 1 -->
  <div class="abs" style="left:0;top:0;width:147px;height:81px;background:var(--teal-soft);padding-top:22px">
    <span class="icon icon-light" style="width:20px;height:20px" role="img" aria-label="Mandala-Symbol"></span>
    <div class="slogan" style="margin-top:5px">Erlebe und erfahre, wie Tantra dein Weg der<br>Trantsformation zu mehr Freude, Lebendig-<br>keit, Erfolg, Kraft, Liebe und Lust werden kann.</div>
  </div>
  <div class="photo" role="img" aria-label="Foto: Hände bei einer Massage auf rotem Tuch" style="left:0;top:81px;width:147px;height:92px;opacity:.75"></div>
  <svg class="wave" style="top:162px" width="147" height="14" viewBox="0 0 147 14"><path d="M0 8 Q40 0 80 6 T147 3 V14 H0Z" fill="#fbfbfb"/><path d="M0 8 Q40 0 80 6 T147 3" fill="none" stroke="var(--teal-soft)" stroke-width="2"/></svg>
  <div class="portrait" role="img" aria-label="Porträtfoto einer Lehrerin" style="left:8px;top:189px;width:38px;height:38px;opacity:.8"></div>
  <div class="intro" style="left:53px;top:190px;width:86px;color:#999">Du findest uns an unterschiedlichen Standorten Deutschlands und in deiner Stadt, wenn du dieses Faltblatt gefunden hast.<br><br>Für unsere Angebote mieten wir geeignete Räume in Berlin, Leipzig, Hamburg, Dresden und bald in deiner Stadt.</div>
  <div class="contact" style="left:14px;top:240px;color:var(--teal-soft)">
    <h5>Kontakt:</h5>
    <div><i style="background:var(--teal-soft)"></i>www.lichtung-tantra.de</div>
    <div><i style="background:var(--teal-soft)"></i>0151 23 45 67 80</div>
    <div><i style="background:var(--teal-soft)"></i>Tantrisches.Bildungszentrum.HausDerLichtung</div>
    <div><i style="background:var(--teal-soft)"></i>HausDerLichtung</div>
  </div>
  <div class="network" style="left:12px;top:295px;color:var(--orange-soft)">Wir sind ein wachsendes Netzwerk aus mehreren Lehrern.</div>

  <!-- panels 2–3 -->
  <div class="abs" style="left:147px;top:0;width:1px;height:331px;background:#d8d8d8"></div>
  <div class="abs" style="left:277px;top:0;width:1px;height:331px;background:#d8d8d8"></div>
  <div class="photo" role="img" aria-label="Foto: Massage-Szene auf gemusterten Kissen in warmem Orange" style="left:147px;top:0;width:262px;height:108px;background:radial-gradient(circle at 45% 30%,#f4b04c,#d6802c 45%,#6e2a18)"></div>
  <svg class="wave" style="left:147px;top:86px" width="262" height="26" viewBox="0 0 262 26"><path d="M0 16 Q70 4 130 12 T262 6 V26 H0Z" fill="#f8f8f7"/><path d="M0 16 Q70 4 130 12 T262 6" fill="none" stroke="var(--teal-soft)" stroke-width="2"/></svg>
  <div class="card" style="left:155px;top:108px;width:115px;text-align:left">
    <h3 style="text-align:center;margin-bottom:3px">Berufs-Ausbildungen</h3>
    <p class="body" style="margin:0">Mach Tantra zu deinem Beruf!<br>Investiere zwei bis fünf wundervolle Jahre je nach deiner Wahl in eine Berufsausbildung mit Zukunft!</p>
    <p class="body">Unser Tantra Bildungszentrum bietet sechs berufsbegleitende Ausbildungen an:</p>
    <p class="body" style="padding-left:26px;text-align:left">1. Tantra-Lehrer<br>2. Tantra-Yoga-Lehrer<br>3. Tantrischer Massagetherapeut<br>4. Tantrischer Sexualtherapeut<br>5. Tantra-Coach<br>6. Selbst Ausbilder werden</p>
    <p class="body">Die Voraussetzungen zur Teilnahme an der Ausbildung sind der Abschluss des von uns angebotenen Level 1 der Tantraausbildung sowie des Jahrestrainings (Level 2). Während der Ausbildung wirst du zunächst Assistenzen in Gruppen des Levels 1 sowie in Gruppen des Jahrestrainings durchführen. Für deine spätere Begleitung eigener Gruppen erhältst du Supervision von uns. Wenn du die Ausbildung erfolgreich abgeschlossen hast, bist du herzlich willkommen im Team des Bildungszentrums mitzuwirken.</p>
    <p class="body">Mehr Infos über die Inhalte und Termine der Berufsausbildungen, erhalst du bei unserem Vortrag über berufliche Perspektiven.</p>
  </div>
  <div class="card" style="left:284px;top:116px;width:117px">
    <span class="icon icon-orange" style="width:22px;height:22px" role="img" aria-label="Mandala-Symbol"></span>
    <h3 style="margin-top:5px">Werde unsere Mitarbeiter</h3>
    <p class="body">Du möchtest selbst haupt- oder nebenberuflich mit Tantra arbeiten? Wir laden dich ein, dich als Mitarbeiter in unserem Bildungszentrum „Haus der Lichtung" zu bewerben. Bist du ein Tantra- oder Yogalehrer und hast schon eigene Erfahrungen beim Organisieren und Unterrichten von Gruppen gesammelt? Hast du Freude im Team mit anderen Tantralehrern und anderen Experten zusammenzuarbeiten und die Botschaften von Tantra in die Welt zu tragen, damit diese mehr und mehr Menschen erreichen. Falls ja, würden wir uns freuen, wenn du dich bei uns bewirbst, als Tantra- oder Yogalehrer zu unterrichten. Wir laden dich auch ein, in unserem Bildungszentrum zu wirken wenn du noch keine Ausbildung im tantrischen Bereich gemacht hast, dies aber gerne tun möchtest. Wir bieten eine Auswahl an unterschiedlichen Ausbildungen an und begleiten dich gern in deinen neuen Beruf auf tantrischem Gebiet.</p>
  </div>
  <div class="abs" style="left:290px;top:263px;display:flex;gap:5px;align-items:center">
    <span class="brand-dot" style="width:12px;height:12px"></span>
    <span style="font-size:4.6px;font-weight:700;color:var(--teal);line-height:1.3">Bewerbe dich bei Marta Ulrich unter:<br><span style="color:var(--orange)">marta.ulrich@lichtung-tantra.de</span></span>
  </div>
  <div class="footline" style="left:185px;top:298px"><span class="brand-dot" style="width:6px;height:6px"></span><b style="font-size:4.6px">Haus der Lichtung</b> Alle Termine und Angebote findest du auch hier: <span>www.lichtung-tantra.de</span></div>

  <!-- panel 4 -->
  <div class="abs" style="left:409px;top:0;width:116px;height:331px;background:linear-gradient(90deg,#f7f7f6,#ececeb)">
    <div class="brand" style="left:20px;top:30px">
      <span class="brand-dot" style="background:var(--orange-soft)"></span>
      <span class="brand-text" style="font-size:7px;color:var(--teal-soft)"><small style="font-size:5px;font-weight:400;color:var(--orange-soft)">Bildungszentrum</small>Haus der Lichtung</span>
    </div>
    <div class="photo" role="img" aria-label="Rundes Foto eines Paares in warmem Licht, umgeben von orangefarbenem Mandala" style="left:24px;top:78px;width:64px;height:64px;border-radius:50%;border:2px solid var(--orange-soft);opacity:.85"></div>
    <svg class="wave" style="top:150px" width="116" height="16" viewBox="0 0 116 16"><path d="M0 8 Q30 16 60 9 T116 2 V16 H0Z" fill="var(--teal-soft)"/><path d="M0 7 Q30 15 60 8 T116 1" fill="none" stroke="var(--orange-soft)" stroke-width="1.5"/></svg>
    <div class="abs" style="left:0;top:165px;width:116px;height:166px;background:var(--teal-soft);display:flex;flex-direction:column;align-items:center;gap:7px;padding-top:6px">
      <span class="icon icon-light" role="img" aria-label="Mandala-Symbol"></span>
      <div class="slogan" style="font-weight:400">Tantra als Weg der<br>Transformation</div>
      <span class="icon icon-light" role="img" aria-label="Mandala-Symbol"></span>
      <div class="slogan" style="font-weight:400">Verändere durch Tantra<br>dein Leben, deine Beziehungen,<br>dein Job!</div>
      <span class="icon icon-light" role="img" aria-label="Mandala-Symbol"></span>
      <div class="slogan" style="font-weight:400">Nutze Tantra für mehr Erfolg,<br>Kraft, Energie und Lust am Leben!</div>
    </div>
  </div>
</section>

</div>
</body>
</html>
```